lifestyle photographer promotion piece

I would like to create a printed postcard to send to potential clients to introduce them to my work and hopefully create new clients. I'm a commercial photographer who just relocated to the Miami area and would really like to be getting more luxury lifestyle and resort work that includes my unique ability to shoot every aspect of lifestyle including food, travel, lifestyle and fashion. I'd like to incorporate between 4-12 of my best images from my online portfolio at www.delphinecarrow.com. The printed piece should also have a very clean, graphic, modern feel to it overall similar to my website. The main goal is to create a striking and compelling grouping of images showing my diverse offerings but in a way that shows an obvious visual style, my style. Please refer to my website for images. When winner is chosen, I will supply hi-res files to compete the design.
Updates

The card is a mailer and a handout. The back of the card should be black and white and text only with my info and an area for address to information. Dimensions of the card are 6x8.5 inches and I prefer the horizontal aspect ratio.

I've noticed a few designers are incorporating graphics. I would like to avoid that. Interested in photography dominated card with /or without graphic use of white space. I tend to avoid color backgrounds, white space is my preference in most cases although I'm not completely against it. 

Target Market(s)

Advertising Agencies and Magazines, Record Labels, Modeling Agencies, Public Relations Firms

Industry/Entity Type

Fashion

Requirements
Must have
• Horizontal

Front(color):
Delphine Carrow Photography
Miami / Naples / New York

Back(black and white):
(239)614-2958
www.delphinecarrow.com
info@delphinecarrow.com

```html
<!DOCTYPE html>
<html lang="en">
<head>
<meta charset="utf-8">
<title>Delphine Carrow Photography – Postcard Back</title>
<link href="https://fonts.googleapis.com/css2?family=Questrial&display=swap" rel="stylesheet">
<style>
  :root {
    --paper: #fcfcfc;
    --pattern-tone: #f4f4f4;
    --ink: #1a1a1a;
    --rule: #2a2a2a;
    --divider: #6e6e6e;
  }
  html, body {
    margin: 0;
    padding: 0;
    width: 1200px;
    height: 847px;
    overflow: hidden;
    background: var(--paper);
  }
  .postcard-back {
    position: relative;
    width: 1200px;
    height: 847px;
    overflow: hidden;
    font-family: "Questrial", sans-serif;
    color: var(--ink);
  }
  .background-pattern {
    position: absolute;
    inset: 0;
    background: radial-gradient(ellipse at center, var(--pattern-tone) 0%, var(--paper) 75%);
  }
  .studio-name {
    position: absolute;
    left: 30px;
    top: 22px;
    margin: 0;
    font-family: "Questrial", sans-serif;
    font-weight: 400;
    font-size: 42px;
    line-height: 50px;
    color: var(--ink);
    letter-spacing: 1px;
  }
  .studio-name span { display: block; }
  .contact-details {
    position: absolute;
    left: 22px;
    top: 752px;
    margin: 0;
    font-size: 19.5px;
    line-height: 25.5px;
    letter-spacing: 1px;
    color: var(--ink);
  }
  .contact-details p { margin: 0; }
  .postcard-frame {
    position: absolute;
    inset: 0;
  }
</style>
</head>
<body>
  <main class="postcard-back">
    <div class="background-pattern" role="img" aria-label="Faint light-grey damask swirl pattern across the card"></div>

    <h1 class="studio-name"><span>Delphine Carrow</span><span>Photography</span></h1>

    <address class="contact-details">
      <p>(239)614-2958</p>
      <p>www.delphinecarrow.com</p>
      <p>info@delphinecarrow.com</p>
    </address>

    <svg class="postcard-frame" width="1200" height="847" viewBox="0 0 1200 847" aria-hidden="true">
      <line class="message-divider" x1="702.5" y1="57" x2="702.5" y2="797" stroke="var(--divider)" stroke-width="1.5"/>
      <rect class="stamp-box" x="999.5" y="46.5" width="157" height="178" rx="8" ry="8" fill="none" stroke="var(--ink)" stroke-width="3"/>
      <g class="address-lines" stroke="var(--rule)" stroke-width="1.2">
        <line x1="758" y1="366.5" x2="1163" y2="366.5"/>
        <line x1="758" y1="450.5" x2="1163" y2="450.5"/>
        <line x1="758" y1="535.5" x2="1163" y2="535.5"/>
        <line x1="762" y1="619.5" x2="1159" y2="619.5"/>
      </g>
    </svg>
  </main>
</body>
</html>
```